Simple AD for Digital Publication

Total Size 5" x 5", may include boarder or not
Image Provided; crop or use as background
Incorporate Logo and text as provided

Target Market(s)

Sound Contractors / Integrators

Industry/Entity Type

Audio Video Lighting

Requirements
Must have
• Bold Look that reflects our brand. see website: tovermundic.com - cohesive text and style

```html
<!DOCTYPE html>
<html lang="en">
<head>
<meta charset="UTF-8">
<title>Protect and Conceal – Dealer Ad</title>
<link rel="stylesheet" href="https://fonts.googleapis.com/css2?family=Oswald:wght@700&family=Roboto+Condensed:ital,wght@0,400;0,700;1,700&display=swap">
<style>
  :root {
    --page-bg: #1a1a1a;
    --photo-deep: #3a0b10;
    --photo-mid: #8e2420;
    --photo-warm: #c4502e;
    --silver-light: #f2f2f2;
    --silver-dark: #8d9093;
    --outline: #3b3b3b;
    --bar-black: #0a0a0a;
    --band-light: #f4f4f5;
    --band-grey: #c9cacc;
    --brand-red: #c8242a;
    --brand-deep: #5c1014;
    --ink: #3d3d3f;
    --white: #ffffff;
  }
  * { margin: 0; padding: 0; box-sizing: border-box; }
  html, body { width: 1200px; height: 978px; overflow: hidden; background: var(--page-bg); }
  .ad {
    position: absolute; left: 111px; top: 0;
    width: 978px; height: 978px; overflow: hidden;
    font-family: "Roboto Condensed", sans-serif;
  }
  .ad__photo {
    position: absolute; left: 0; top: 0; width: 978px; height: 740px;
    background:
      radial-gradient(ellipse at 80% 15%, rgba(230,150,60,.55), transparent 45%),
      radial-gradient(ellipse at 15% 20%, rgba(200,60,40,.5), transparent 50%),
      linear-gradient(160deg, var(--photo-mid) 0%, var(--photo-warm) 45%, var(--photo-deep) 100%);
  }
  .ad__bolts { position: absolute; left: 735px; top: 60px; }
  .headline { position: absolute; left: 97px; font-family: "Oswald", sans-serif; font-weight: 700; text-transform: uppercase; line-height: 1; }
  .headline span {
    display: inline-block; transform-origin: left top;
    background: linear-gradient(180deg, var(--silver-light) 0%, #d5d6d8 45%, var(--silver-dark) 100%);
    -webkit-background-clip: text; background-clip: text; color: transparent;
    -webkit-text-stroke: 2px var(--outline);
  }
  .headline--top { top: 168px; font-size: 122px; }
  .headline--top span { transform: scaleX(0.86); letter-spacing: -2px; }
  .headline--main { top: 268px; font-size: 228px; }
  .headline--main span { transform: scaleX(0.76); letter-spacing: -3px; -webkit-text-stroke: 3px var(--outline); }
  .subline {
    position: absolute; left: 97px; top: 495px; width: 730px; height: 54px;
    background: var(--bar-black); color: var(--white);
    font-style: italic; font-weight: 700; font-size: 37px; line-height: 54px;
    padding-left: 22px; letter-spacing: -0.3px;
  }
  .band {
    position: absolute; left: 0; top: 740px; width: 978px; height: 151px;
    background: linear-gradient(180deg, var(--band-light) 0%, #e2e3e4 55%, var(--band-grey) 100%);
  }
  .footer {
    position: absolute; left: 0; top: 891px; width: 978px; height: 87px;
    background: linear-gradient(90deg, var(--brand-red) 0%, #8e1a1e 45%, var(--brand-deep) 100%);
  }
  .dealer { position: absolute; left: 100px; top: 654px; width: 292px; height: 248px; display: block; text-decoration: none; }
  .dealer__shape { position: absolute; left: 0; top: 0; display: block; }
  .dealer__lead, .dealer__title, .dealer__button {
    position: absolute; left: 0; width: 292px; display: block;
    text-align: center; color: var(--white); line-height: 1;
  }
  .dealer__lead { top: 95px; font-size: 19px; font-weight: 400; }
  .dealer__title { top: 114px; font-size: 42px; font-weight: 700; }
  .dealer__button {
    left: 56px; top: 157px; width: 180px; height: 39px;
    background: var(--brand-red); border: 2px solid var(--white); border-radius: 3px;
    font-size: 28px; font-weight: 700; line-height: 35px;
  }
  .brand { position: absolute; left: 436px; top: 790px; display: flex; align-items: center; gap: 14px; }
  .brand__mark { width: 58px; height: 58px; background: var(--ink); }
  .brand__name { font-weight: 700; font-size: 40px; line-height: 1; color: var(--ink); letter-spacing: -0.5px; }
  .brand__tag { font-size: 18px; color: var(--ink); margin-top: 2px; }
</style>
</head>
<body>
<main class="ad">
  <div class="ad__photo" role="img" aria-label="Photo of string lights and cables running into a stage floor pocket on a wooden stage, in warm red tones"></div>

  <svg class="ad__bolts" width="170" height="140" viewBox="0 0 170 140" aria-hidden="true">
    <polygon points="80,0 30,55 55,55 20,95 70,45 48,45" fill="#e6e6e6"/>
    <polygon points="160,45 95,95 125,95 70,140 140,88 110,88" fill="#e6e6e6"/>
  </svg>

  <h1 class="headline headline--top"><span>Protect and</span></h1>
  <h1 class="headline headline--main"><span>Conceal</span></h1>
  <p class="subline">HIGH AND LOW VOLTAGE CONNECTIVITY</p>

  <div class="band"></div>
  <div class="footer"></div>

  <a class="dealer" href="#">
    <svg class="dealer__shape" width="292" height="248" viewBox="0 0 292 248" aria-hidden="true">
      <defs>
        <linearGradient id="dealerFill" x1="0" y1="0" x2="0" y2="1">
          <stop offset="0" stop-color="#9c2126"/>
          <stop offset="1" stop-color="#4a0d10"/>
        </linearGradient>
      </defs>
      <path d="M132,8 Q146,-4 160,8 L282,122 Q292,132 282,142 L190,246 L102,246 L10,142 Q0,132 10,122 Z"
            fill="url(#dealerFill)" stroke="#ffffff" stroke-width="3"/>
      <g fill="#ffffff" transform="translate(124,42)">
        <polygon points="4,14 24,4 24,32 4,22"/>
        <rect x="0" y="13" width="6" height="10"/>
        <rect x="8" y="22" width="5" height="12"/>
        <path d="M28,10 l8,-6 M30,18 h10 M28,26 l8,6" stroke="#ffffff" stroke-width="2"/>
      </g>
    </svg>
    <span class="dealer__lead">BECOME A</span>
    <span class="dealer__title">DEALER</span>
    <span class="dealer__button">CLICK HERE</span>
  </a>

  <div class="brand">
    <div class="brand__mark"></div>
    <div>
      <div class="brand__name">TOVERMUNDIC CO</div>
      <div class="brand__tag">Stage Pocket Systems Connectivity</div>
    </div>
  </div>
</main>
</body>
</html>
```